Letterhead Design Project

I need a letterhead design that is simple, modern, and colorful.

We publish novels that speak to female empowerment. With our fiction, we hope to encourage women to live boldly and love themselves without apology.

Our logo is red and teal so I'd like to see those colors continued in the letterhead.

The final design should be bold and inspiring.
Updates

Hello talented designers!

We will also be needing a business card design which will hopefully go to the designer of our letterhead. Please keep that in mind.

Thanks for all your efforts (in advance)!

I'd like the following information included:

Address - 4716 North Pellham Street, Suite #208, Fernbrook Falls, Oregon 97381
Website - www.quillmarshpress.example
Email - info@quillmarshpress.example

Please see the updated files. The part of the logo that was red is now pink. And I've uploaded .eps and .ai formats. Thanks.

Target Market(s)

women, age 25+, college educated professionals

Requirements
Nice to have
• swirls or flourishes
Should not have
• dots or stripes

```html
<!DOCTYPE html>
<html lang="en">
<head>
<meta charset="utf-8">
<title>Quillmarsh Press – Stationery</title>
<link rel="stylesheet" href="https://fonts.googleapis.com/css2?family=Crimson+Text:ital@0;1&family=Open+Sans:wght@400&display=swap">
<style>
  :root {
    --pink: #e0197d;
    --ink: #2f3a4e;
    --teal: #3b7d8c;
    --paper: #ffffff;
    --backdrop: #e4e5e7;
    --shadow: rgba(0, 0, 0, 0.18);
  }
  * { box-sizing: border-box; margin: 0; padding: 0; }
  html, body { width: 1200px; height: 1200px; overflow: hidden; }
  body {
    background: var(--backdrop);
    position: relative;
    font-family: "Crimson Text", Georgia, serif;
    color: var(--ink);
  }
  address { font-style: normal; }

  /* Letterhead */
  .letterhead {
    position: absolute;
    left: 70px; top: 110px;
    width: 600px; height: 776px;
    background: var(--paper);
    box-shadow: 0 4px 18px var(--shadow);
  }
  .letterhead-header {
    position: absolute;
    left: 36px; right: 36px; top: 30px;
    display: flex; justify-content: space-between; align-items: flex-start;
    gap: 16px;
  }
  .brand { display: flex; align-items: center; gap: 10px; }
  .brand-dot {
    width: 26px; height: 26px; border-radius: 50%;
    background: var(--pink); flex: none;
  }
  .brand-name {
    font-size: 24px; color: var(--pink); line-height: 1;
  }
  .brand-tagline {
    font-size: 11.5px; color: var(--ink); margin-top: 3px; letter-spacing: 0.2px;
  }
  .letterhead-contact {
    border-left: 1.5px solid var(--pink);
    padding-left: 10px;
    font-size: 9.5px; line-height: 1.45;
    color: var(--ink);
    white-space: nowrap;
  }
  .letterhead-contact .web { color: var(--pink); margin-top: 5px; }
  .letterhead-contact .web + .web { margin-top: 0; }
  .letterhead-rule {
    position: absolute; left: 36px; right: 36px; top: 96px;
    height: 1.5px; background: var(--pink);
  }
  .letterhead-footer-rule {
    position: absolute; right: 36px; bottom: 28px;
    width: 320px; height: 1.5px; background: var(--pink);
  }

  /* Business card */
  .business-card {
    position: absolute;
    left: 720px; top: 540px;
    width: 420px; height: 240px;
    background: var(--paper);
    box-shadow: 0 4px 18px var(--shadow);
    padding: 26px 26px 22px;
    display: flex; flex-direction: column; justify-content: space-between;
  }
  .business-card .brand-name { font-size: 26px; }
  .business-card .brand-tagline { color: var(--teal); font-size: 13px; }
  .card-contact {
    font-family: "Open Sans", Arial, sans-serif;
    font-size: 14px; line-height: 1.35;
    color: #1d1d1f;
  }
  .card-contact .web { color: var(--pink); }
</style>
</head>
<body>

  <section class="letterhead" aria-label="Letterhead">
    <header class="letterhead-header">
      <div class="brand">
        <span class="brand-dot"></span>
        <div>
          <div class="brand-name">Quillmarsh Press</div>
          <div class="brand-tagline">Every reader deserves a brave story of her own.</div>
        </div>
      </div>
      <address class="letterhead-contact">
        <div>4716 North Pellham Street,</div>
        <div>Suite #208, Fernbrook Falls, Oregon 97381</div>
        <div class="web">Website - www.quillmarshpress.example</div>
        <div class="web">Email - info@quillmarshpress.example</div>
      </address>
    </header>
    <div class="letterhead-rule"></div>
    <div class="letterhead-footer-rule"></div>
  </section>

  <section class="business-card" aria-label="Business card">
    <div class="brand">
      <span class="brand-dot"></span>
      <div>
        <div class="brand-name">Quillmarsh Press</div>
        <div class="brand-tagline">Every reader deserves a brave story of her own.</div>
      </div>
    </div>
    <address class="card-contact">
      <div>4716 North Pellham Street,</div>
      <div>Suite #208, Fernbrook Falls, Oregon 97381</div>
      <div class="web">www.quillmarshpress.example</div>
      <div class="web">info@quillmarshpress.example</div>
    </address>
  </section>

</body>
</html>
```